Business Card Design

RETAIL HIGH END CONTEMPORARY WOMEN'S CLOTHING STORE
MODERN, SIMPLE, CLEAN, COOL

WE ARE ALL ABOUT NY and CALIF STYLE.... CLASSY but EDGY..
COOLEST DENIM , Trendsetting, NEUTRAL Pallettes,
Collections : Thread and Ivy, Corvin Dace, MPW, K47, GVD
Don't need names of collections on card. thats just good info
for designer of card.

WOULD LIKE THE FONT TO BE INTERESTING, but CLEAN
We are on facebook daily with photos of outfits we put together
which you can look up and friend us.... MellowDuneShop
Also on instagram .
Open to options on color and size, but need cool and fresh.

Industry/Entity Type

Business

Contact Information for Business Card

LORNA 5471 Harbor Ave. #318 Cedarline Court Shoppes..Va. Beach, Va. 23987
Phone 757.610.4825 Fax 757.610-3392 EMAIL..LORNABOUTIQUE@MAILVERO.COM

```html
<!DOCTYPE html>
<html lang="en">
<head>
<meta charset="utf-8">
<title>Lorna Business Card</title>
<link rel="stylesheet" href="https://fonts.googleapis.com/css2?family=Alegreya:wght@400&family=Comfortaa:wght@400&display=swap">
<style>
  :root {
    --backdrop-edge: #ae2629;
    --backdrop-glow: #b97c80;
    --card-dark: #0a0c12;
    --card-navy: #161b2a;
    --panel-green-light: #00980f;
    --panel-green-dark: #045604;
    --brand-green: #0a9a12;
    --text-white: #ffffff;
    --icon-black: #000000;
  }
  * { margin: 0; padding: 0; box-sizing: border-box; }
  html, body {
    width: 1200px;
    height: 900px;
    overflow: hidden;
  }
  body {
    background: radial-gradient(ellipse 560px 480px at 600px 420px, var(--backdrop-glow) 0%, var(--backdrop-edge) 100%);
    font-family: "Alegreya", Georgia, serif;
    position: relative;
  }
  .business-card {
    position: absolute;
    left: 240px;
    top: 283px;
    width: 673px;
    height: 359px;
    background: radial-gradient(ellipse 500px 300px at 260px 20px, var(--card-navy) 0%, var(--card-dark) 100%);
    overflow: hidden;
  }
  .brand-name {
    position: absolute;
    left: 138px;
    top: 254px;
    height: 96px;
    transform: rotate(-90deg);
    transform-origin: 0 100%;
    font-family: "Comfortaa", "Trebuchet MS", sans-serif;
    font-size: 96px;
    line-height: 96px;
    color: var(--brand-green);
    font-weight: 400;
    white-space: nowrap;
  }
  .contact-panel {
    position: absolute;
    left: 142px;
    top: 28px;
    right: 0;
    bottom: 0;
    background: radial-gradient(ellipse 300px 230px at 290px 200px, var(--panel-green-light) 0%, var(--panel-green-dark) 100%);
  }
  .contact-row {
    position: absolute;
    left: 17px;
    display: flex;
    align-items: flex-start;
    color: var(--text-white);
    font-size: 27px;
    line-height: 36px;
  }
  .contact-icon {
    width: 35px;
    height: 35px;
    background: var(--icon-black);
    flex: none;
    margin-right: 17px;
    display: block;
  }
  .row-address { top: 56px; }
  .row-phone { top: 184px; }
  .row-fax { top: 232px; }
  .row-email { top: 282px; }
  .row-address .contact-text { margin-top: 5px; }
  .row-phone .contact-text,
  .row-fax .contact-text,
  .row-email .contact-text { margin-top: -1px; }
  .row-phone .contact-text { margin-left: 3px; }
</style>
</head>
<body>
  <section class="business-card">
    <div class="contact-panel">
      <div class="contact-row row-address">
        <svg class="contact-icon" viewBox="0 0 35 35" aria-label="Address">
          <rect width="35" height="35" fill="#000"/>
          <g stroke="#fff" stroke-width="3.4" stroke-linecap="square">
            <line x1="15" y1="5" x2="11" y2="29"/>
            <line x1="24" y1="5" x2="20" y2="29"/>
            <line x1="7" y1="12.5" x2="28" y2="12.5"/>
            <line x1="6" y1="21.5" x2="27" y2="21.5"/>
          </g>
        </svg>
        <div class="contact-text">5471 Harbor Ave<br>318 Cedarline Court Shoppes<br>Va. Beach, Va. 23987</div>
      </div>
      <div class="contact-row row-phone">
        <svg class="contact-icon" viewBox="0 0 35 35" aria-label="Phone">
          <rect width="35" height="35" fill="#000"/>
          <path d="M4 13 Q17.5 4 31 13 L29 17 L24 15.5 L24 12.5 Q17.5 10.5 11 12.5 L11 15.5 L6 17 Z" fill="#fff"/>
          <path d="M10 17 L25 17 L29 28 L6 28 Z" fill="#fff"/>
          <circle cx="17.5" cy="22.5" r="3" fill="#000"/>
        </svg>
        <div class="contact-text">757.610.4825</div>
      </div>
      <div class="contact-row row-fax">
        <svg class="contact-icon" viewBox="0 0 35 35" aria-label="Fax">
          <rect width="35" height="35" fill="#000"/>
          <rect x="13" y="4" width="14" height="11" fill="#fff"/>
          <rect x="4" y="13" width="6" height="18" fill="#fff"/>
          <rect x="11" y="15" width="20" height="16" fill="#fff"/>
          <g fill="#000">
            <rect x="14" y="18" width="3" height="2.5"/><rect x="19" y="18" width="3" height="2.5"/><rect x="24" y="18" width="3" height="2.5"/>
            <rect x="14" y="22.5" width="3" height="2.5"/><rect x="19" y="22.5" width="3" height="2.5"/><rect x="24" y="22.5" width="3" height="2.5"/>
            <rect x="14" y="27" width="3" height="2"/><rect x="19" y="27" width="3" height="2"/><rect x="24" y="27" width="3" height="2"/>
          </g>
        </svg>
        <div class="contact-text">757.610-3392</div>
      </div>
      <div class="contact-row row-email">
        <svg class="contact-icon" viewBox="0 0 35 35" aria-label="Email">
          <rect width="35" height="35" fill="#000"/>
          <rect x="3" y="8" width="29" height="19" fill="#fff"/>
          <polyline points="3,8 17.5,19 32,8" fill="none" stroke="#000" stroke-width="1.6"/>
          <line x1="3" y1="27" x2="13" y2="16" stroke="#000" stroke-width="1.2"/>
          <line x1="32" y1="27" x2="22" y2="16" stroke="#000" stroke-width="1.2"/>
        </svg>
        <div class="contact-text">lornaboutique@mailvero.com</div>
      </div>
    </div>
    <div class="brand-name">Lorna</div>
  </section>
</body>
</html>
```